Commercial Construction Company Looking to Revamp Image

Varnholt Construction Co., Inc. has been in business for 20 years, and is a mid sized commercial construction company looking to update our image to reflect a more modern corporate culture, but to still reflect traditional core values in construction, such as dependability, honesty, and solid workmanship. Our largest clients include government and public agencies who seek companies with the aforementioned values, but are open to new ideas and innovations. We have used a dark blue and white to represent us in the past and would like for this color scheme to continue as not to isolate our existing customers. The addition of a gray is acceptable. Please see our previous business card. *It is imperative to retain the logo as closely as possible.* There is a possibility to shorten the name of the company to "VCCI," dependent on design concepts, or possible integration of the acronym to our existing name.

Industry/Entity Type

Business

```html
<!DOCTYPE html>
<html lang="en">
<head>
<meta charset="utf-8">
<title>Varnholt Construction Co., Inc. — Business Card</title>
<link rel="stylesheet" href="https://fonts.googleapis.com/css2?family=Arimo:wght@400;700&display=swap">
<style>
  :root {
    --backdrop: #2a2a2a;
    --brand-blue: #2c4f8a;
    --brand-white: #ffffff;
    --rule-gray: #6e6e6e;
    --muted-gray: #555b66;
    --card-shadow: rgba(0, 0, 0, 0.55);
  }
  * { box-sizing: border-box; margin: 0; padding: 0; }
  html, body {
    width: 1200px;
    height: 900px;
    overflow: hidden;
    background: var(--backdrop);
    font-family: "Arimo", Arial, sans-serif;
  }
  .stage {
    width: 1200px;
    height: 900px;
    display: flex;
    align-items: center;
    justify-content: center;
    gap: 40px;
  }
  .card {
    width: 500px;
    height: 286px;
    position: relative;
    overflow: hidden;
    box-shadow: 0 12px 30px var(--card-shadow);
  }

  /* Front side */
  .card-front { background: var(--brand-blue); }
  .front-top {
    position: absolute;
    left: 0; top: 0;
    width: 100%;
    height: 128px;
    background: var(--brand-white);
    border-bottom: 5px solid var(--rule-gray);
  }
  .wordmark {
    position: absolute;
    left: 34px;
    top: 70px;
    display: flex;
    align-items: center;
    gap: 10px;
  }
  .wordmark-square {
    width: 44px;
    height: 44px;
    background: var(--brand-blue);
    border-radius: 4px;
  }
  .wordmark-name {
    color: var(--brand-blue);
    font-weight: 700;
    font-size: 15px;
    line-height: 1.15;
    text-transform: uppercase;
    letter-spacing: 0.3px;
  }
  .holder {
    position: absolute;
    right: 34px;
    top: 28px;
    text-align: right;
  }
  .holder-name {
    color: var(--brand-blue);
    font-weight: 700;
    font-size: 14px;
  }
  .holder-title {
    color: var(--muted-gray);
    font-size: 10px;
    margin-top: 2px;
  }
  .phones {
    position: absolute;
    right: 34px;
    top: 150px;
    list-style: none;
    text-align: right;
    color: var(--brand-white);
    font-size: 11px;
    line-height: 1.65;
  }
  .address {
    position: absolute;
    left: 34px;
    bottom: 26px;
    color: var(--brand-white);
    font-style: normal;
    font-size: 12px;
    line-height: 1.6;
  }

  /* Back side */
  .card-back {
    background: var(--brand-blue);
    display: flex;
    align-items: center;
    justify-content: center;
  }
  .back-mark {
    display: flex;
    align-items: center;
    gap: 14px;
  }
  .back-square {
    width: 58px;
    height: 58px;
    background: var(--brand-white);
    border-radius: 8px;
  }
  .back-name {
    color: var(--brand-white);
    font-weight: 700;
    font-size: 24px;
    line-height: 1.1;
    text-transform: uppercase;
    letter-spacing: 0.5px;
  }
</style>
</head>
<body>
  <main class="stage">
    <section class="card card-front" aria-label="Business card front">
      <div class="front-top"></div>
      <div class="wordmark">
        <span class="wordmark-square"></span>
        <span class="wordmark-name">Varnholt<br>Construction Co., Inc.</span>
      </div>
      <div class="holder">
        <p class="holder-name">Anton Varnholt</p>
        <p class="holder-title">President</p>
      </div>
      <ul class="phones">
        <li>Office : (555) 201 4410</li>
        <li>Fax : (555) 201 4418</li>
        <li>Cell : (555) 306 7723</li>
      </ul>
      <address class="address">
        41-43 Garner Avenue<br>
        Linden Falls, N.J. 07190<br>
        varnholtconstruction@mailbox.com
      </address>
    </section>

    <section class="card card-back" aria-label="Business card back">
      <div class="back-mark">
        <span class="back-square"></span>
        <span class="back-name">Varnholt<br>Construction</span>
      </div>
    </section>
  </main>
</body>
</html>
```